Modern Lawfirm Business Card Design

We're looking for a business card to incorporate the newly created logo we had made.

Ideally looking for a law firm business card demonstrating, modern, minimalist, strong/bold design.

I'm open to any design honestly, but nothing "flashy".

Target Market(s)

Immigration law, family immigration, humanitarian, general legal

Industry/Entity Type

Law Firm

Contact Information for Business Card

Please use dummy information, name, street address, city, state, phone number, email, website.

Font styles to use
Serif
Sans Serif

Requirements
Must have
• Please use dummy information, name, street address, city, state, phone number, email, website.

```html
<!DOCTYPE html>
<html lang="en">
<head>
<meta charset="utf-8">
<title>Castellan Immigration Law – Business Card</title>
<link rel="stylesheet" href="https://fonts.googleapis.com/css2?family=Tinos:wght@400;700&display=swap">
<style>
  :root {
    --brand-blue: #03599f;
    --paper: #ffffff;
    --backdrop: #d9d9d9;
    --ink-blue: #0a5aa0;
  }
  * { margin: 0; padding: 0; box-sizing: border-box; }
  html, body { width: 1200px; height: 1200px; overflow: hidden; }
  body {
    background: var(--backdrop);
    font-family: "Tinos", "Times New Roman", serif;
    position: relative;
  }
  .card {
    position: absolute;
    left: 376px;
    width: 448px;
    height: 256px;
    overflow: hidden;
  }
  .card--front { top: 214px; background: var(--brand-blue); }
  .card--back { top: 672px; background: var(--paper); }

  .wordmark { position: absolute; text-align: center; font-weight: 400; }
  .wordmark__name { display: block; letter-spacing: 0.02em; line-height: 1; }
  .wordmark__tag { display: block; letter-spacing: 0.42em; line-height: 1; }

  .card--front .wordmark {
    left: 0; right: 0; top: 98px; color: var(--paper);
  }
  .card--front .wordmark__name { font-size: 46px; }
  .card--front .wordmark__tag { font-size: 9px; margin-top: 6px; }

  .card--back .wordmark {
    left: 32px; top: 30px; color: var(--brand-blue); text-align: left;
  }
  .card--back .wordmark__name { font-size: 27px; }
  .card--back .wordmark__tag { font-size: 5.5px; margin-top: 4px; }

  .contact {
    position: absolute;
    right: 42px;
    top: 106px;
    text-align: right;
    color: var(--ink-blue);
  }
  .contact__name { font-size: 24px; line-height: 1; }
  .contact__title { font-size: 8px; margin-top: 3px; margin-bottom: 10px; }
  .contact__list { list-style: none; font-size: 12px; line-height: 14.5px; }
  .contact__item { position: relative; }
  .contact__icon {
    position: absolute;
    right: -17px;
    top: 3px;
    width: 9px;
    height: 9px;
  }
  .contact__item--plain .contact__icon { display: none; }

  .footer-band { position: absolute; left: 0; bottom: 0; width: 448px; height: 18px; }
</style>
</head>
<body>

  <section class="card card--front" aria-label="Card front">
    <div class="wordmark">
      <span class="wordmark__name">CASTELLAN</span>
      <span class="wordmark__tag">IMMIGRATION LAW</span>
    </div>
  </section>

  <section class="card card--back" aria-label="Card back">
    <div class="wordmark">
      <span class="wordmark__name">CASTELLAN</span>
      <span class="wordmark__tag">IMMIGRATION LAW</span>
    </div>

    <div class="contact">
      <p class="contact__name">Your Name</p>
      <p class="contact__title">Your Tittle</p>
      <ul class="contact__list">
        <li class="contact__item">2280 Harbor Crest Avenue Suite
          <svg class="contact__icon" viewBox="0 0 10 10"><rect width="10" height="10" rx="2" fill="var(--brand-blue)"/><path d="M5 2 L8 5 H6.5 V8 H3.5 V5 H2 Z" fill="#fff"/></svg>
        </li>
        <li class="contact__item contact__item--plain">410 Dallas, TX 75201</li>
        <li class="contact__item">(214) 555-0148
          <svg class="contact__icon" viewBox="0 0 10 10"><rect width="10" height="10" rx="2" fill="var(--brand-blue)"/><path d="M3 2 L4.5 2 L5 4 L4 4.6 Q4.8 6 6 6.4 L6.6 5.5 L8 6 L8 7.5 Q5 8 3 5 Q2.4 3.5 3 2 Z" fill="#fff"/></svg>
        </li>
        <li class="contact__item">info@castellanlaw.com
          <svg class="contact__icon" viewBox="0 0 10 10"><rect width="10" height="10" rx="2" fill="var(--brand-blue)"/><rect x="2" y="3" width="6" height="4.2" fill="none" stroke="#fff" stroke-width="0.8"/><path d="M2 3 L5 5.4 L8 3" fill="none" stroke="#fff" stroke-width="0.8"/></svg>
        </li>
        <li class="contact__item">www.castellanlaw.com
          <svg class="contact__icon" viewBox="0 0 10 10"><rect width="10" height="10" rx="2" fill="var(--brand-blue)"/><circle cx="5" cy="5" r="2.8" fill="none" stroke="#fff" stroke-width="0.8"/><path d="M2.2 5 H7.8 M5 2.2 V7.8" stroke="#fff" stroke-width="0.6"/></svg>
        </li>
      </ul>
    </div>

    <svg class="footer-band" viewBox="0 0 448 18" preserveAspectRatio="none" aria-hidden="true">
      <rect width="448" height="18" fill="var(--brand-blue)"/>
      <polygon points="270,18 300,0 332,0 302,18" fill="var(--paper)"/>
    </svg>
  </section>

</body>
</html>
```